Vital Spark Electrical in need of a business card design

We need a new business card designed for our electrical business. We have a logo already which I will attach below.
Would like the business card to be..
-BLACK background preferably, possibly white back ground behind logo if colours clash.
-White & Blue (logo blue) text
Something that makes the logo pop, & a modern look. Possibly minimal clean format.

REQUIRE:
-Logo on front & back

TEXT TO INCLUDE (ON ONE SIDE):

Tom Harlow
Director/Electrician
M: 0417 365 208
E:info@vitalsparkelectrical-example.com.au
W:www.vitalsparkelectrical-example.com.au
R.E.C 57318

Custom/New Homes
Renovations
Commercial Office/Shop Fit-outs
Communications & Security Cameras
Electric Vehicle Chargers
Airconditioning
Updates

Requirements
Nice to have
• Possibly even lighten the grey shades for the words 'Vital' & 'Spark' to be more easily read on a black background.

```html
<!DOCTYPE html>
<html lang="en">
<head>
<meta charset="utf-8">
<title>Vital Spark Electrical – Business Card</title>
<link rel="stylesheet" href="https://fonts.googleapis.com/css2?family=Poppins:wght@400;500;600&display=swap">
<style>
  :root {
    --stage: #1f1f21;
    --card: #141415;
    --card-edge: #1c1c1e;
    --white: #f2f4f6;
    --grey: #aab2bb;
    --muted: #c9ced4;
    --blue: #1aa3e8;
  }
  * { box-sizing: border-box; margin: 0; padding: 0; }
  html, body {
    width: 1200px; height: 1200px; overflow: hidden;
    background: var(--stage);
    font-family: "Poppins", sans-serif;
  }
  .stage {
    width: 1200px; height: 1200px;
    display: flex; flex-direction: column; align-items: center; justify-content: center;
    gap: 40px;
  }
  .card {
    position: relative;
    width: 900px; height: 514px;
    background: var(--card);
    border: 1px solid var(--card-edge);
    border-radius: 22px;
    overflow: hidden;
  }

  /* Back side */
  .card--back { display: flex; align-items: center; justify-content: center; }
  .brand {
    display: flex; align-items: center; gap: 16px;
  }
  .brand__mark {
    width: 20px; height: 20px; background: var(--blue);
  }
  .brand__name {
    font-weight: 600; letter-spacing: 0.5px; white-space: nowrap;
  }
  .card--back .brand__name { font-size: 40px; color: var(--white); }

  /* Front side */
  .card--front .brand { position: absolute; left: 64px; top: 64px; }
  .card--front .brand__name { font-size: 34px; color: var(--grey); }

  .person {
    position: absolute; right: 64px; top: 150px; text-align: right;
  }
  .person__name { font-size: 30px; font-weight: 600; color: var(--grey); line-height: 1.15; }
  .person__role { font-size: 22px; font-weight: 400; color: var(--blue); }

  .services {
    position: absolute; left: 64px; top: 200px; list-style: none;
  }
  .services li {
    display: flex; align-items: center; gap: 14px;
    font-size: 20px; color: var(--muted); line-height: 31px;
  }
  .services li::before {
    content: ""; width: 9px; height: 9px; background: var(--blue); flex: none;
  }

  .contacts {
    position: absolute; right: 64px; top: 306px;
    display: flex; flex-direction: column; align-items: flex-end; gap: 6px;
  }
  .contacts__row {
    display: flex; align-items: center; gap: 14px;
    font-size: 18px; color: var(--white);
  }
  .contacts__row svg { width: 20px; height: 20px; flex: none; }

  .footer-rule {
    position: absolute; left: 0; right: 0; bottom: 52px;
    display: flex; align-items: center; gap: 16px;
  }
  .footer-rule__line { height: 3px; background: var(--blue); }
  .footer-rule__line--long { flex: 1; }
  .footer-rule__line--short { width: 64px; }
  .licence { font-size: 20px; color: var(--white); white-space: nowrap; }
</style>
</head>
<body>
<main class="stage">
  <section class="card card--back" aria-label="Card back">
    <div class="brand">
      <span class="brand__mark"></span>
      <span class="brand__name">Vital Spark Electrical</span>
    </div>
  </section>

  <section class="card card--front" aria-label="Card front">
    <div class="brand">
      <span class="brand__mark"></span>
      <span class="brand__name">Vital Spark Electrical</span>
    </div>

    <div class="person">
      <p class="person__name">Tom Harlow</p>
      <p class="person__role">Director/Electrician</p>
    </div>

    <ul class="services">
      <li>Custom/New Homes</li>
      <li>Renovations</li>
      <li>Commercial Office/Shop Fit-outs</li>
      <li>Communications &amp; Security Cameras</li>
      <li>Electric Vehicle Chargers</li>
      <li>Airconditioning</li>
    </ul>

    <div class="contacts">
      <p class="contacts__row">0417 365 208
        <svg viewBox="0 0 24 24" aria-hidden="true"><path d="M6.6 10.8a15.1 15.1 0 0 0 6.6 6.6l2.2-2.2c.3-.3.7-.4 1-.2 1.1.4 2.3.6 3.6.6.6 0 1 .4 1 1V20c0 .6-.4 1-1 1A17 17 0 0 1 3 4c0-.6.4-1 1-1h3.5c.6 0 1 .4 1 1 0 1.3.2 2.5.6 3.6.1.3 0 .7-.2 1z" fill="var(--blue)"/></svg>
      </p>
      <p class="contacts__row">info@vitalsparkelectrical-example.com.au
        <svg viewBox="0 0 24 24" aria-hidden="true"><rect x="2" y="5" width="20" height="14" rx="1" fill="var(--blue)"/><path d="M2.5 6l9.5 7 9.5-7" stroke="var(--card)" stroke-width="1.6" fill="none"/></svg>
      </p>
      <p class="contacts__row">www.vitalsparkelectrical-example.com.au
        <svg viewBox="0 0 24 24" aria-hidden="true" fill="none" stroke="var(--blue)" stroke-width="1.8"><circle cx="12" cy="12" r="9"/><ellipse cx="12" cy="12" rx="4" ry="9"/><path d="M3 12h18M4.5 7.5h15M4.5 16.5h15"/></svg>
      </p>
    </div>

    <div class="footer-rule">
      <span class="footer-rule__line footer-rule__line--long"></span>
      <span class="licence">R.E.C 57318</span>
      <span class="footer-rule__line footer-rule__line--short"></span>
    </div>
  </section>
</main>
</body>
</html>
```